Billboard design - consider what a billboard is

Design a billboard using my logo - Billboard is 6m x 3m
A Billboard is advertising for my company that is on a big sign.

Has to be clean and easy to read, and ideally highlights that we are Residential and Commercial builders.

Keep it clean and easy to read

The contact number for the board is

022 583 7092
www.harbourframeworks.co.nz
info@harbourframeworks.co.nz

Doesnt have to have all contact details if it doesnt fit

Has to catch peoples attention to contact us if they need a builder

Can you please change the sign to be all white writing, with black background ?
Updates

Please consider what a billboard is...

The design needs to be suitable for a billboard..

Target Market(s)

people driving past

Industry/Entity Type

Construction

Logo Text

Harbour Builder, website email address, contact number

Colors
0054AA
0677BA
7BADD7
CADEEF
E8F1F8

Requirements
Must have
• Easy to read
Nice to have
• easy to read, can clearly see contact details

```html
<!DOCTYPE html>
<html lang="en">
<head>
<meta charset="utf-8">
<title>Harbour Builder Billboard</title>
<link href="https://fonts.googleapis.com/css2?family=Poppins:wght@500;600;700&display=swap" rel="stylesheet">
<style>
  :root {
    --page: #e8eef4;
    --white: #ffffff;
    --title-blue: #0f5e92;
    --tag-blue: #1a6a9c;
    --navy: #0c3a5e;
    --mid-blue: #125c8c;
    --band-blue: #1a7db8;
    --brand-2: #0677ba;
    --brand-3: #7badd7;
    --brand-4: #cadeef;
  }
  * { margin: 0; padding: 0; box-sizing: border-box; }
  html, body {
    width: 1200px;
    height: 1200px;
    overflow: hidden;
    background: var(--page);
    font-family: "Poppins", sans-serif;
  }
  .canvas {
    width: 1200px;
    height: 1200px;
    display: flex;
    align-items: center;
    justify-content: center;
  }
  .billboard {
    position: relative;
    width: 1200px;
    height: 600px;
    background: var(--white);
    overflow: hidden;
  }
  .feature-graphic {
    position: absolute;
    left: 560px;
    top: 60px;
    width: 640px;
    height: 540px;
    background: linear-gradient(180deg, var(--brand-4) 0%, var(--brand-3) 40%, var(--brand-2) 100%);
  }
  .base-block {
    position: absolute;
    left: 360px;
    top: 396px;
    width: 200px;
    height: 204px;
    background: var(--mid-blue);
  }
  .brand-name {
    position: absolute;
    left: 44px;
    top: 40px;
    color: var(--title-blue);
    font-weight: 700;
    font-size: 124px;
    line-height: 118px;
    letter-spacing: -3px;
  }
  .tagline {
    position: absolute;
    left: 48px;
    top: 318px;
    color: var(--tag-blue);
    font-weight: 500;
    font-size: 34px;
  }
  .phone-band {
    position: absolute;
    left: 0;
    top: 404px;
    width: 360px;
    height: 100px;
    background: var(--navy);
    display: flex;
    align-items: center;
    padding-left: 44px;
  }
  .phone {
    color: var(--white);
    font-weight: 600;
    font-size: 46px;
    letter-spacing: -0.5px;
  }
  .web-band {
    position: absolute;
    left: 0;
    top: 504px;
    width: 420px;
    height: 96px;
    background: var(--band-blue);
    display: flex;
    align-items: center;
    padding-left: 44px;
  }
  .website {
    color: var(--white);
    font-weight: 500;
    font-size: 21px;
  }
</style>
</head>
<body>
<main class="canvas">
  <section class="billboard">
    <div class="feature-graphic" role="img" aria-label="Abstract blue building-block skyline graphic"></div>
    <div class="base-block"></div>

    <h1 class="brand-name">Harbour<br>Builder</h1>
    <p class="tagline">Residential &amp; Commercial</p>

    <div class="phone-band">
      <p class="phone">022 583 7092</p>
    </div>
    <div class="web-band">
      <p class="website">www.harbourframeworks.co.nz</p>
    </div>
  </section>
</main>
</body>
</html>
```